Window and GutterCleaning Flyer A5 size double sided.

We need a double sided A5 flyer. Side 1, is for window cleaning, side 2 is for gutter cleaning. Licensed by Borough of Halvern Council.
Phone number 0800 315 4720.
Business address 7 Tarnlow Brae, North Pellin Edinburgh EH14 3RW.
www.clearpane-vista-services.com
We use a LoftPro Gutter inspection Cam to view your gutters first to see if they need doing.
Window cleaning ; Professional window cleaning services, what we offer, water fed pole window cleaning able to reach windows up to 60 feet.
Conservatory cleaning.
Conservatory roof cleaning.
Fascias & Soffits cleaning.
Excellent Customer Service.
Target Market(s)
domestic houses
Industry/Entity Type
window cleaning
Look and feel
Each slider illustrates characteristics of the customer's brand and the style your logo design should communicate.

```html
<!DOCTYPE html>
<html lang="en">
<head>
<meta charset="utf-8">
<title>ClearPane Vista Services – A5 Flyer</title>
<link rel="stylesheet" href="https://fonts.googleapis.com/css2?family=Poppins:wght@400;500;600;700;800;900&display=swap">
<style>
:root{
  --navy:#26255f;
  --sky:#9ec4ec;
  --paper:#f1f3f9;
  --stage:#d6d6d6;
  --white:#ffffff;
  --line:#3a3a78;
}
*{box-sizing:border-box;margin:0;padding:0}
html,body{width:1200px;height:2746px;overflow:hidden}
body{background:var(--stage);font-family:'Poppins',sans-serif;color:var(--navy);position:relative}
.page{position:absolute;left:160px;width:880px;height:1247px;background:linear-gradient(180deg,#f4f6fb,#eceff7);overflow:hidden;box-shadow:0 4px 14px rgba(0,0,0,.18)}
.page--front{top:84px}
.page--back{top:1415px}
.abs{position:absolute}

.brand{position:absolute;left:594px;top:60px;width:210px;display:flex;align-items:center;gap:10px}
.brand__mark{width:18px;height:18px;background:var(--navy);flex:none}
.brand__name{font-weight:800;font-size:30px;line-height:1.05;color:var(--navy);font-family:'Poppins',sans-serif}

.photo{position:absolute}
.roof{position:absolute;left:0;top:0;width:880px;height:1247px;pointer-events:none}

/* front */
.hero-band{left:0;top:296px;width:880px;height:289px;background:var(--sky)}
.hero-photo{left:0;top:0;width:640px;height:585px;clip-path:polygon(0 222px,212px 34px,487px 277px,487px 296px,640px 296px,640px 585px,0 585px);background:linear-gradient(90deg,#6f5a4f 0%,#8b7e78 45%,#a9b3c4 75%,rgba(158,196,236,0) 100%)}
.hero-title{right:33px;top:322px;text-align:right;font-weight:900;font-size:41px;line-height:48px;text-transform:uppercase;letter-spacing:.2px}
.section-bar{left:0;top:585px;width:880px;height:45px;background:var(--navy);color:var(--sky);font-weight:600;font-size:21px;letter-spacing:5px;text-align:center;line-height:45px}
.service{position:absolute;width:300px;text-align:center;font-size:22px;line-height:25px;font-weight:500}
.service__icon{width:74px;height:74px;border-radius:50%;background:var(--sky);margin:0 auto 10px;display:flex;align-items:center;justify-content:center}
.divider{position:absolute;width:2px;background:var(--navy)}
.strip{top:992px;width:194px;height:141px}
.tagline{left:0;top:1144px;width:880px;text-align:center;font-size:21px;font-weight:500}
.tagline b{font-weight:800;text-transform:uppercase}

.footer{position:absolute;left:0;width:880px;height:45px;display:flex}
.footer__addr{width:298px;font-size:13px;line-height:15px;text-align:center;padding-top:7px;font-weight:500}
.footer__contact{flex:1;background:var(--navy);color:var(--white);display:flex;align-items:center;padding-left:22px}
.footer__phone{font-weight:800;font-size:27px;display:flex;align-items:center;gap:6px;width:240px}
.footer__web{font-size:15px;display:flex;align-items:center;gap:7px}
.page--front .footer{top:1186px}
.page--front .footer__addr{background:var(--sky)}
.page--back .footer{top:1185px}
.page--back .footer__addr{background:var(--white)}

/* back */
.back-title{left:39px;top:42px;font-weight:900;font-size:38px;line-height:46px;text-transform:uppercase}
.copy{left:40px;top:281px;width:476px;font-size:14.4px;line-height:17.6px;text-align:justify}
.copy p{margin-bottom:17px}
.gutter-photo{left:554px;top:264px;width:281px;height:388px;background:linear-gradient(160deg,#7b8a73,#5c6a55 50%,#9aa1a5)}
.cam-photo{left:560px;top:663px;width:273px;height:282px;background:radial-gradient(circle at 50% 45%,#3b4858 0%,#2a2a2a 60%,rgba(42,42,42,0) 72%)}
.cam-band{left:0;top:960px;width:880px;height:225px;background:var(--sky)}
.leaf-photo{left:0;top:0;width:600px;height:1185px;clip-path:polygon(0 927px,212px 708px,487px 945px,487px 960px,600px 960px,600px 1185px,0 1185px);background:linear-gradient(90deg,#8a6a3c 0%,#a7865a 40%,#b9b5ad 75%,rgba(158,196,236,0) 100%)}
.cam-note{left:597px;top:980px;width:270px;font-weight:600;font-size:27px;line-height:30px}
.cam-note__rule{left:579px;top:978px;width:4px;height:180px;background:var(--navy)}
</style>
</head>
<body>

<section class="page page--front">
  <div class="abs hero-band"></div>
  <div class="photo hero-photo" role="img" aria-label="Window cleaner using a water fed pole on a house conservatory"></div>
  <svg class="roof" viewBox="0 0 880 1247"><polyline points="0,222 212,34 487,277 880,277" fill="none" stroke="var(--navy)" stroke-width="18" stroke-linejoin="miter"/></svg>

  <div class="brand"><span class="brand__mark"></span><span class="brand__name">ClearPane Vista</span></div>

  <h1 class="abs hero-title">High-quality,<br>professional<br>window cleaning<br>service across<br>west Edinburgh</h1>

  <div class="abs section-bar">WINDOW CLEANING SERVICES WE OFFER</div>

  <div class="service" style="left:-21px;top:659px">
    <div class="service__icon"><svg width="40" height="40" viewBox="0 0 40 40" fill="var(--navy)"><rect x="10" y="5" width="20" height="32"/><rect x="4" y="16" width="6" height="21"/><rect x="30" y="16" width="6" height="21"/><g fill="var(--sky)"><rect x="13" y="9" width="4" height="4"/><rect x="23" y="9" width="4" height="4"/><rect x="13" y="17" width="4" height="4"/><rect x="23" y="17" width="4" height="4"/><rect x="13" y="25" width="4" height="4"/><rect x="23" y="25" width="4" height="4"/></g></svg></div>
    High-reach<br>window cleaning
  </div>
  <div class="service" style="left:296px;top:659px">
    <div class="service__icon"><svg width="40" height="40" viewBox="0 0 40 40"><rect x="8" y="5" width="24" height="30" fill="var(--navy)"/><rect x="12" y="9" width="16" height="22" fill="var(--sky)"/><rect x="19" y="9" width="3" height="22" fill="var(--navy)"/><rect x="5" y="34" width="30" height="3" fill="var(--navy)"/></svg></div>
    Conservatory Windows<br>&amp; Frames cleaning
  </div>
  <div class="service" style="left:614px;top:659px">
    <div class="service__icon"><svg width="44" height="40" viewBox="0 0 44 40" fill="var(--navy)"><polygon points="22,5 42,22 36,22 22,11 8,22 2,22"/><polygon points="9,23 22,13 35,23 35,33 9,33"/></svg></div>
    Conservatory<br>roof cleaning
  </div>
  <div class="service" style="left:120px;top:818px">
    <div class="service__icon"><svg width="44" height="40" viewBox="0 0 44 40" fill="var(--navy)"><polygon points="4,16 40,4 40,9 4,21"/><rect x="7" y="22" width="4" height="13"/><rect x="14" y="20" width="4" height="15"/><rect x="21" y="17" width="4" height="18"/><rect x="28" y="15" width="4" height="20"/><rect x="35" y="12" width="4" height="23"/></svg></div>
    Fascias &amp;<br>Soffits cleaning
  </div>
  <div class="service" style="left:482px;top:818px">
    <div class="service__icon"><svg width="44" height="40" viewBox="0 0 44 40" fill="var(--navy)"><polygon points="22,3 24,9 30,9 25,13 27,19 22,15 17,19 19,13 14,9 20,9"/><polygon points="10,9 11,12 14,12 12,14 13,17 10,15 7,17 8,14 6,12 9,12"/><polygon points="34,9 35,12 38,12 36,14 37,17 34,15 31,17 32,14 30,12 33,12"/><path d="M3 26 h9 l6 3 h8 a2 2 0 0 1 0 4 h-8 l9 0 9-6 a2 2 0 0 1 3 3 l-11 8 h-16 l-9 -3z"/></svg></div>
    Excellent<br>Customer Service
  </div>

  <div class="divider" style="left:269px;top:644px;height:151px"></div>
  <div class="divider" style="left:631px;top:644px;height:151px"></div>
  <div class="divider" style="left:446px;top:824px;height:148px"></div>

  <div class="photo strip" style="left:38px;background:linear-gradient(180deg,#b6c8dc,#e8edf2 50%,#8a5b3f)" role="img" aria-label="Clean white conservatory"></div>
  <div class="photo strip" style="left:240px;background:linear-gradient(150deg,#f3f3f3,#d3d5d8 60%,#7e4f3a)" role="img" aria-label="White soffit boards under a roof"></div>
  <div class="photo strip" style="left:443px;background:linear-gradient(120deg,#5c6470,#c7ccd2 55%,#8d949b)" role="img" aria-label="Water fed pole brush on a window"></div>
  <div class="photo strip" style="left:646px;background:linear-gradient(170deg,#6f86b5,#4c6396 55%,#8aa0c8)" role="img" aria-label="Pole brush spraying water"></div>

  <p class="abs tagline">water fed pole window cleaning able to <b>reach windows up to 60 feet</b></p>

  <footer class="footer">
    <div class="footer__addr">7 Tarnlow Brae,<br>North Pellin Edinburgh EH14 3RW</div>
    <div class="footer__contact">
      <span class="footer__phone"><svg width="18" height="18" viewBox="0 0 24 24" fill="#fff"><path d="M6.6 10.8a15 15 0 0 0 6.6 6.6l2.2-2.2a1 1 0 0 1 1-.25 11.4 11.4 0 0 0 3.6.57 1 1 0 0 1 1 1V20a1 1 0 0 1-1 1A17 17 0 0 1 3 4a1 1 0 0 1 1-1h3.5a1 1 0 0 1 1 1c0 1.25.2 2.45.57 3.57a1 1 0 0 1-.25 1z"/></svg>0800 315 4720</span>
      <span class="footer__web"><svg width="15" height="15" viewBox="0 0 24 24" fill="none" stroke="#fff" stroke-width="2"><circle cx="12" cy="12" r="10"/><path d="M2 12h20M12 2c3 3 3 17 0 20M12 2c-3 3-3 17 0 20"/></svg>www.clearpane-vista-services.com</span>
    </div>
  </footer>
</section>

<section class="page page--back">
  <h2 class="abs back-title">Residential and<br>commercial<br>fast and easy<br>gutter cleaning<br>service</h2>

  <div class="brand"><span class="brand__mark"></span><span class="brand__name">ClearPane Vista</span></div>

  <div class="abs copy">
    <p>Gutters are an important part of your home. Letting your gutters get blocked up can cause damage to your property, so why not set up an annual plan and make sure you don’t run into problems when winter comes.</p>
    <p>Over time your gutters will fill up with moss, leaves and other unwanted debris which will affect the appearance of your home. When gutters aren’t cleared and emptied on a regular basis they become heavy and risk pulling away from the fascias.</p>
    <p>When gutters are not clear it can also lead to blockages in the gutters and downpipes, which will cause the water to overflow. The water which overflows from the guttering can lead to damp problems and other problems in the structure of your property which can become a costly repair.</p>
    <p>We recommend gutters to be cleared out once a year. If your gutters are blocked and overflowing, why not contact us for a free no obligation quote to clear them out and get them working as they should. With our gutter cleaning service we will clear all gutters and unblock all downpipes ensuring the water is running freely and down your drains.</p>
  </div>

  <div class="photo gutter-photo" role="img" aria-label="Gutter vacuum pole clearing a roof gutter"></div>
  <div class="photo cam-photo" role="img" aria-label="Gutter inspection camera with display screen"></div>

  <div class="abs cam-band"></div>
  <div class="photo leaf-photo" role="img" aria-label="Gloved hand removing autumn leaves from a gutter"></div>
  <svg class="roof" viewBox="0 0 880 1247"><polyline points="0,927 212,708 487,952 880,952" fill="none" stroke="var(--navy)" stroke-width="18"/></svg>

  <div class="abs cam-note__rule"></div>
  <p class="abs cam-note">LoftPro<br>Gutter inspection<br>Cam to view your<br>gutters first to see<br>if they need doing</p>

  <footer class="footer">
    <div class="footer__addr">7 Tarnlow Brae,<br>North Pellin Edinburgh EH14 3RW</div>
    <div class="footer__contact">
      <span class="footer__phone"><svg width="18" height="18" viewBox="0 0 24 24" fill="#fff"><path d="M6.6 10.8a15 15 0 0 0 6.6 6.6l2.2-2.2a1 1 0 0 1 1-.25 11.4 11.4 0 0 0 3.6.57 1 1 0 0 1 1 1V20a1 1 0 0 1-1 1A17 17 0 0 1 3 4a1 1 0 0 1 1-1h3.5a1 1 0 0 1 1 1c0 1.25.2 2.45.57 3.57a1 1 0 0 1-.25 1z"/></svg>0800 315 4720</span>
      <span class="footer__web"><svg width="15" height="15" viewBox="0 0 24 24" fill="none" stroke="#fff" stroke-width="2"><circle cx="12" cy="12" r="10"/><path d="M2 12h20M12 2c3 3 3 17 0 20M12 2c-3 3-3 17 0 20"/></svg>www.clearpane-vista-services.com</span>
    </div>
  </footer>
</section>

</body>
</html>
```